Business Card for Bramble Gear

Target Market(s)

Mining, fleet, 4wd industry

Industry/Entity Type

Business

Requirements
Must have
• Front of card
Logo of Bramble Gear, the Nut preferrably top right corner and wording which says
"The Classic Kordo Bolt Products along bottom right hand corner
Use of the orange logo.
Back of card down left side to include (bullet points )
. Canvas Seat Covers
. Hi - Vis Flags
. Canvas or PVC designs by request.
back of card down right side
Danielle Rowbeck
Ph 02 49315728
E ; admin@bramblegear.com.au
W: www.bramblegear.com.au
Nice to have
• other designs can also be submitted as we require additional cards.

```html
<!DOCTYPE html>
<html lang="en">
<head>
<meta charset="utf-8">
<title>Bramble Gear – Business Card (Back)</title>
<link rel="stylesheet" href="https://fonts.googleapis.com/css2?family=Arimo:wght@400&display=swap">
<style>
  :root {
    --card-bg: #ffffff;
    --brand-orange: #f7941d;
    --contact-grey: #808080;
  }
  html, body {
    margin: 0;
    padding: 0;
    width: 1200px;
    height: 734px;
    overflow: hidden;
    background: var(--card-bg);
  }
  .card {
    position: relative;
    width: 1200px;
    height: 734px;
    background: var(--card-bg);
    font-family: "Arimo", Arial, sans-serif;
    font-weight: 400;
  }
  .contact {
    position: absolute;
    right: 69px;
    top: 0;
    text-align: right;
  }
  .contact__name,
  .contact__line {
    position: absolute;
    right: 0;
    margin: 0;
    white-space: nowrap;
    line-height: 1;
  }
  .contact__name {
    top: 79px;
    font-size: 52px;
    color: var(--brand-orange);
  }
  .contact__line {
    font-size: 41px;
    color: var(--contact-grey);
  }
  .contact__line--phone { top: 157px; }
  .contact__line--email { top: 213px; }
  .contact__line--web   { top: 269px; }

  .services {
    list-style: none;
    margin: 0;
    padding: 0;
  }
  .services__item {
    position: absolute;
    left: 137px;
    margin: 0;
    font-size: 39px;
    line-height: 1;
    color: var(--brand-orange);
    white-space: nowrap;
  }
  .services__item::before {
    content: "";
    position: absolute;
    left: -52px;
    top: 15px;
    width: 9px;
    height: 9px;
    border-radius: 50%;
    background: var(--brand-orange);
  }
  .services__item:nth-child(1) { top: 465px; }
  .services__item:nth-child(2) { top: 542px; }
  .services__item:nth-child(3) { top: 618px; }
</style>
</head>
<body>
  <main class="card">
    <section class="contact" aria-label="Contact details">
      <h1 class="contact__name">Danielle Rowbeck</h1>
      <p class="contact__line contact__line--phone">02 4931 5728</p>
      <p class="contact__line contact__line--email">admin@bramblegear.com.au</p>
      <p class="contact__line contact__line--web">www.bramblegear.com.au</p>
    </section>
    <ul class="services" aria-label="Products">
      <li class="services__item">Canvas Seat Covers</li>
      <li class="services__item">Hi–Vis Flags</li>
      <li class="services__item">Canvas or PVC designs by request</li>
    </ul>
  </main>
</body>
</html>
```